Manufacturing company needs new business card.

I need a unique Business Card that will truly stand out. Nothing too busy. Simple is good, right? Not looking for a standard design either. No cookie cutter layout. I am just looking for something interesting and a bit different. Does't have to completely off the wall crazy, just not your run of the mill business card. Clean and modern with a touch of industrial.

Target Market(s)

Air conditioning industry, Architects, builders.

Industry/Entity Type

Business

Contact Information for Business Card

Details to be included on card are:

Peter Walsh
Managing Director

T: 1300 418 592
M: 0427 385 914
W: www.brandvalefabrication.com.au
E: peter.walsh@brandvalefabrication.com.au
A: 58 Harlow Lane, Sydney NSW 2000

Font styles to use
Sans Serif

Colors
0355a3
848484
fbfbfb

Requirements
Must have
• Card design must be landscape.

```html
<!DOCTYPE html>
<html lang="en">
<head>
<meta charset="utf-8">
<title>Brandvale Fabrication – Business Card</title>
<link rel="stylesheet" href="https://fonts.googleapis.com/css2?family=Open+Sans:wght@400;600;700&display=swap">
<style>
  :root {
    --brand-blue: #0355a3;
    --card-blue: #1d4fa6;
    --card-blue-deep: #17448f;
    --bevel-light: #a9bde3;
    --bevel-mid: #6f8fcf;
    --brand-grey: #848484;
    --text-grey: #555555;
    --card-white: #fbfbfb;
    --page-bg: #e9e9e9;
  }
  * { margin: 0; padding: 0; box-sizing: border-box; }
  html, body {
    width: 1200px;
    height: 900px;
    overflow: hidden;
    background: var(--page-bg);
    font-family: "Open Sans", Arial, sans-serif;
  }
  .canvas {
    width: 1200px;
    height: 900px;
    display: flex;
    align-items: center;
    justify-content: center;
    gap: 30px;
  }
  .card {
    position: relative;
    width: 555px;
    height: 339px;
    border-radius: 4px;
    overflow: hidden;
    box-shadow: 0 6px 18px rgba(0,0,0,0.18);
  }

  /* Front */
  .card-front { background: var(--card-white); }
  .front-panel {
    position: absolute;
    top: 0; right: 0;
    width: 225px;
    height: 100%;
    background: linear-gradient(135deg, var(--card-blue) 0%, var(--card-blue-deep) 100%);
  }
  .front-panel-bevel {
    position: absolute;
    top: 0; left: 0;
    width: 14px;
    height: 100%;
    background: linear-gradient(90deg, var(--bevel-light) 0%, var(--bevel-mid) 100%);
  }
  .front-content {
    position: absolute;
    left: 34px;
    top: 42px;
    width: 290px;
  }
  .company-name {
    font-size: 24px;
    font-weight: 600;
    color: var(--brand-blue);
    letter-spacing: -0.3px;
    white-space: nowrap;
  }
  .company-rule {
    width: 150px;
    height: 1.5px;
    background: var(--brand-grey);
    margin-top: 10px;
  }
  .person { margin-top: 28px; }
  .person-name {
    font-size: 20px;
    font-weight: 600;
    color: var(--brand-blue);
    line-height: 1.1;
  }
  .person-title {
    font-size: 12px;
    color: var(--text-grey);
    margin-top: 2px;
  }
  .contact-list {
    list-style: none;
    margin-top: 18px;
  }
  .contact-item {
    display: flex;
    align-items: center;
    gap: 7px;
    font-size: 12.5px;
    color: var(--text-grey);
    line-height: 20px;
    white-space: nowrap;
  }
  .contact-icon {
    width: 11px;
    height: 11px;
    flex: none;
    fill: var(--brand-blue);
  }

  /* Back */
  .card-back {
    background: var(--card-blue);
    display: flex;
    align-items: center;
    justify-content: center;
  }
  .back-lockup {
    display: flex;
    align-items: center;
    gap: 16px;
  }
  .back-mark {
    width: 36px;
    height: 36px;
    background: #ffffff;
  }
  .back-name {
    font-size: 27px;
    font-weight: 600;
    color: #ffffff;
    letter-spacing: -0.3px;
  }
</style>
</head>
<body>
<main class="canvas">

  <section class="card card-front" aria-label="Business card front">
    <div class="front-panel" role="img" aria-label="Large bevelled brand symbol decoration in blue and grey">
      <div class="front-panel-bevel"></div>
    </div>
    <div class="front-content">
      <div class="company-name">Brandvale Fabrication</div>
      <div class="company-rule"></div>

      <div class="person">
        <div class="person-name">Peter Walsh</div>
        <div class="person-title">Managing Director</div>
      </div>

      <ul class="contact-list">
        <li class="contact-item">
          <svg class="contact-icon" viewBox="0 0 24 24" aria-hidden="true"><path d="M3 9c0-3 4-5 9-5s9 2 9 5v2h-5V9c-1-.6-2.4-1-4-1s-3 .4-4 1v2H3z"/><path d="M6 13h12l2 7H4z"/></svg>
          1300 418 592
        </li>
        <li class="contact-item">
          <svg class="contact-icon" viewBox="0 0 24 24" aria-hidden="true"><path d="M7 1h10a2 2 0 0 1 2 2v18a2 2 0 0 1-2 2H7a2 2 0 0 1-2-2V3a2 2 0 0 1 2-2zm0 3v14h10V4zm5 15.5a1.2 1.2 0 1 0 0 2.4 1.2 1.2 0 0 0 0-2.4z"/></svg>
          0427 385 914
        </li>
        <li class="contact-item">
          <svg class="contact-icon" viewBox="0 0 24 24" aria-hidden="true"><circle cx="12" cy="12" r="11"/></svg>
          www.brandvalefabrication.com.au
        </li>
        <li class="contact-item">
          <svg class="contact-icon" viewBox="0 0 24 24" aria-hidden="true"><path d="M1 5h22v14H1z"/><path d="M1 5l11 8 11-8" fill="none" stroke="#fbfbfb" stroke-width="2"/></svg>
          peter.walsh@brandvalefabrication.com.au
        </li>
        <li class="contact-item">
          <svg class="contact-icon" viewBox="0 0 24 24" aria-hidden="true"><path d="M12 1a8 8 0 0 0-8 8c0 6 8 14 8 14s8-8 8-14a8 8 0 0 0-8-8zm0 11a3 3 0 1 1 0-6 3 3 0 0 1 0 6z"/></svg>
          58 Harlow Lane, Sydney NSW 2000
        </li>
      </ul>
    </div>
  </section>

  <section class="card card-back" aria-label="Business card back">
    <div class="back-lockup">
      <div class="back-mark"></div>
      <div class="back-name">Brandvale Fabrication</div>
    </div>
  </section>

</main>
</body>
</html>
```